Pest Control Company needs business card!

Hi there, we need a business card designed for our new Pest Control Company. Ideally this card will be simple, yet feel elegant and high end. We want to use the colours Orange, Black and White. Please see our attached logo for the exact colours.

Business card details:

Phone - 0438 517 264
Name - Gus Halloran
Email - Info@trueguardpest.com.au

We would also like to include the following list with dot points:

SERVICES / INSPECTIONS

Termites, Wood Borers, Ants, Cockroaches, Spiders, Fleas, Mice, Rats, Bed Bugs, & More!

```html
<!DOCTYPE html>
<html lang="en">
<head>
<meta charset="utf-8">
<title>Trueguard Pest Control – Business Card</title>
<link href="https://fonts.googleapis.com/css2?family=Montserrat:wght@700;800&family=Roboto:wght@400;500&display=swap" rel="stylesheet">
<style>
  :root {
    --backdrop: #3a3431;
    --card: #262626;
    --orange: #f7931e;
    --orange-deep: #f07a14;
    --red: #e8232a;
    --white: #ffffff;
  }
  * { box-sizing: border-box; margin: 0; padding: 0; }
  html, body { width: 1200px; height: 716px; overflow: hidden; }
  body {
    background: var(--backdrop);
    font-family: "Roboto", Arial, sans-serif;
    color: var(--white);
    position: relative;
  }
  .card {
    position: absolute;
    top: 187px;
    width: 560px;
    height: 342px;
    background: var(--card);
    box-shadow: 0 10px 24px rgba(0,0,0,.45);
    overflow: hidden;
  }
  .card--back { left: 25px; }
  .card--front { left: 615px; }

  /* Back: services list */
  .service-list {
    position: absolute;
    left: 46px;
    top: 34px;
    list-style: none;
    font-size: 15px;
    line-height: 26px;
    letter-spacing: .3px;
    text-transform: uppercase;
  }
  .service-list li::before {
    content: "";
    display: inline-block;
    width: 6px; height: 6px;
    border-radius: 50%;
    background: var(--orange);
    margin-right: 9px;
    vertical-align: middle;
    position: relative; top: -2px;
  }
  .mascot-area {
    position: absolute;
    left: 270px;
    top: 40px;
    width: 240px;
    height: 260px;
    border-radius: 50%;
    background: radial-gradient(circle at 45% 45%, var(--orange), var(--orange-deep));
  }

  /* Front: brand + contact */
  .brand {
    position: absolute;
    left: 40px;
    top: 112px;
    width: 210px;
    display: flex;
    align-items: center;
    gap: 12px;
  }
  .brand__name {
    font-family: "Montserrat", Arial, sans-serif;
    font-weight: 800;
    font-size: 28px;
    line-height: 30px;
    color: var(--orange);
    text-transform: uppercase;
  }
  .brand__dot {
    flex: none;
    width: 34px; height: 34px;
    border-radius: 50%;
    background: var(--orange);
  }
  .divider {
    position: absolute;
    left: 272px;
    top: 92px;
    width: 2px;
    height: 150px;
    background: var(--orange);
  }
  .contact {
    position: absolute;
    left: 292px;
    top: 96px;
  }
  .contact__name {
    font-family: "Montserrat", Arial, sans-serif;
    font-weight: 800;
    font-size: 21px;
    color: var(--orange);
    text-transform: uppercase;
    letter-spacing: .3px;
  }
  .contact__role {
    font-size: 16px;
    margin-top: 2px;
    margin-bottom: 18px;
  }
  .contact__line {
    display: flex;
    align-items: center;
    gap: 7px;
    font-size: 15px;
    line-height: 24px;
  }
  .contact__line svg { flex: none; width: 12px; height: 12px; fill: var(--red); }
</style>
</head>
<body>

<section class="card card--back" aria-label="Card back">
  <ul class="service-list">
    <li>Termites</li>
    <li>Wood Borers</li>
    <li>Ants</li>
    <li>Cockroaches</li>
    <li>Spiders</li>
    <li>Fleas</li>
    <li>Mice</li>
    <li>Rats</li>
    <li>Bed Bugs</li>
    <li>&amp; More!</li>
  </ul>
  <div class="mascot-area" role="img" aria-label="Large brand mascot decoration area"></div>
</section>

<section class="card card--front" aria-label="Card front">
  <div class="brand">
    <span class="brand__name">Trueguard Pest Control</span>
    <span class="brand__dot"></span>
  </div>
  <div class="divider"></div>
  <div class="contact">
    <div class="contact__name">Gus Halloran</div>
    <div class="contact__role">President</div>
    <div class="contact__line">
      <svg viewBox="0 0 24 24" aria-hidden="true"><path d="M6.6 10.8a15.1 15.1 0 0 0 6.6 6.6l2.2-2.2a1 1 0 0 1 1-.25 11.4 11.4 0 0 0 3.6.57 1 1 0 0 1 1 1V20a1 1 0 0 1-1 1A17 17 0 0 1 3 4a1 1 0 0 1 1-1h3.5a1 1 0 0 1 1 1c0 1.25.2 2.45.57 3.57a1 1 0 0 1-.25 1z"/></svg>
      <span>0438 517 264</span>
    </div>
    <div class="contact__line">
      <svg viewBox="0 0 24 24" aria-hidden="true"><path d="M2 5h20v14H2z M2 5l10 8 10-8" /></svg>
      <span>Info@trueguardpest.com.au</span>
    </div>
    <div class="contact__line">
      <svg viewBox="0 0 24 24" aria-hidden="true"><circle cx="12" cy="12" r="10"/></svg>
      <span>www.trueguardpest.com.au</span>
    </div>
  </div>
</section>

</body>
</html>
```